I need a label design to go on our jars of honey. Our company is called Quillbrook Honey Co. The type of honey is called Marram Glade Honey. The jars are 1kg. Attached is the label size. Left hand side needs to have nutritional info... as attached. Middle section is our company name, honey type, 1kg & Whangamata, NZ. Right hand side needs to have info as per photo (raw honey etc). I would like to upload more pictures... but I’m unsure how to do this? Thanks, Noreen

Target Market(s)

Honey consumers... families

Industry/Entity Type

Food Production

Colors

Designer to choose colors to be used in the design.

Requirements
Must have
• Nutritional info as per upload
• Type of honey & company name as per upload
• 1kg
• Address
Nice to have
• Similar fonts to upload.
• Possibly background image... floral or beach... very faint though.

```html
<!DOCTYPE html>
<html lang="en">
<head>
<meta charset="utf-8">
<title>Quillbrook Honey Co. – Marram Glade Honey label</title>
<link rel="stylesheet" href="https://fonts.googleapis.com/css2?family=Josefin+Sans:wght@300;400&family=Shadows+Into+Light&family=Lato:wght@400;700&display=swap">
<style>
  :root {
    --ocean-deep: #3a97d0;
    --ocean-mid: #5aaed6;
    --ocean-teal: #7cc0cf;
    --shore-pale: #b4d8d2;
    --panel-bg: rgba(232, 241, 250, 0.9);
    --panel-ink: #2b63a6;
    --panel-ink-strong: #1f4f94;
    --panel-rule: #ffffff;
    --label-white: #ffffff;
  }
  * { margin: 0; padding: 0; box-sizing: border-box; }
  html, body { width: 1200px; height: 480px; overflow: hidden; background: #ffffff; }

  .label {
    position: relative;
    width: 1200px;
    height: 480px;
    overflow: hidden;
    color: var(--label-white);
  }

  .shoreline-backdrop {
    position: absolute;
    inset: 0;
    background:
      linear-gradient(100deg, transparent 0 44%, rgba(232,243,244,0.55) 48%, rgba(232,243,244,0.75) 51%, rgba(232,243,244,0.35) 54%, transparent 58%),
      linear-gradient(90deg, var(--ocean-deep) 0%, var(--ocean-mid) 35%, var(--ocean-teal) 55%, var(--shore-pale) 75%, var(--shore-pale) 100%);
  }

  /* Nutrition panel */
  .nutrition-panel {
    position: absolute;
    left: 27px;
    top: 33px;
    width: 348px;
    height: 414px;
    border-radius: 24px;
    background: var(--panel-bg);
    color: var(--panel-ink);
    font-family: "Lato", sans-serif;
    text-align: center;
  }
  .panel-claim { margin-top: 12px; font-size: 15px; line-height: 18px; }
  .nutrition-table {
    margin: 10px auto 0;
    width: 228px;
    height: 230px;
    border: 1px solid var(--panel-rule);
    text-align: left;
    padding: 10px 10px 0;
    font-size: 10px;
  }
  .nutrition-heading { line-height: 12px; }
  .nutrition-heading strong { font-weight: 400; text-transform: uppercase; }
  .nutrition-divider { border-top: 1px solid var(--panel-rule); margin: 8px -10px 0; }
  .nutrition-grid { display: grid; grid-template-columns: 78px 78px 60px; margin-top: 6px; }
  .col-head { font-size: 7px; line-height: 9px; }
  .nutrient-rows { display: grid; grid-template-columns: 78px 78px 60px; margin-top: 26px; line-height: 15px; }
  .storage-notes { margin-top: 13px; font-size: 10px; line-height: 13.5px; }
  .batch-fields {
    margin: 11px 0 0 60px;
    text-align: left;
    font-size: 11px;
    font-weight: 700;
    color: var(--panel-ink-strong);
    line-height: 14.5px;
  }
  .batch-fields span { display: inline-block; width: 84px; }

  /* Centre brand block */
  .brand-name {
    position: absolute;
    left: 416px;
    top: 32px;
    width: 360px;
    text-align: center;
    font-family: "Josefin Sans", sans-serif;
    font-weight: 400;
    font-size: 42px;
    line-height: 50px;
  }
  .honey-variety {
    position: absolute;
    left: 396px;
    top: 188px;
    width: 400px;
    text-align: center;
    font-family: "Josefin Sans", sans-serif;
    font-weight: 400;
    font-size: 62px;
    line-height: 80px;
  }
  .net-weight, .origin {
    position: absolute;
    left: 416px;
    width: 360px;
    text-align: center;
    font-family: "Josefin Sans", sans-serif;
    font-weight: 300;
  }
  .net-weight { top: 400px; font-size: 14px; letter-spacing: 1px; }
  .origin { top: 432px; font-size: 15px; letter-spacing: 2px; }

  /* Right story block */
  .story-block {
    position: absolute;
    left: 838px;
    top: 30px;
    width: 320px;
    text-align: center;
    font-family: "Shadows Into Light", cursive;
    font-size: 20px;
    line-height: 28px;
  }
  .story-block p { margin-bottom: 26px; }
  .contact-details {
    position: absolute;
    left: 878px;
    top: 382px;
    width: 220px;
    text-align: center;
    font-style: normal;
    font-family: "Shadows Into Light", cursive;
    font-size: 14px;
    line-height: 16px;
  }
</style>
</head>
<body>
<main class="label">
  <div class="shoreline-backdrop" role="img" aria-label="Aerial view of turquoise ocean waves washing onto a pale sandy beach"></div>

  <section class="nutrition-panel">
    <p class="panel-claim">100% New Zealand Honey<br>no added ingredients</p>
    <div class="nutrition-table">
      <p class="nutrition-heading"><strong>Nutritional information</strong><br>Serving per package: 100<br>Serving size: 10g</p>
      <div class="nutrition-divider"></div>
      <div class="nutrition-grid">
        <span></span>
        <span class="col-head">Average<br>Quantity<br>per serving</span>
        <span class="col-head">Average<br>Quantity<br>per 100g</span>
      </div>
      <div class="nutrient-rows">
        <span>Energy</span><span>134kj</span><span>1340kj</span>
        <span>Protein</span><span>0.04g</span><span>0.4g</span>
        <span>Fat total</span><span>0g</span><span>0g</span>
        <span>- saturated</span><span>0g</span><span>0g</span>
        <span>Carbohydrate</span><span>7.9g</span><span>79.6g</span>
        <span>-sugars</span><span>7.8g</span><span>78.1g</span>
        <span>Sodium</span><span>1.2mg</span><span>12mg</span>
      </div>
    </div>
    <p class="storage-notes">Store upright in a cool, dry place.<br>No refrigeration needed.<br>Not recommended for infants below<br>the age of 12 months</p>
    <p class="batch-fields">
      <span>Best Before</span>:<br>
      <span>RMP</span>:<br>
      <span>Batch No</span>:
    </p>
  </section>

  <h1 class="brand-name">Quillbrook<br>Honey Co.</h1>
  <h2 class="honey-variety">Marram<br>Glade Honey</h2>
  <p class="net-weight">1kg</p>
  <p class="origin">WHANGAMATA, NZ</p>

  <section class="story-block">
    <p>Sourced from the beautiful<br>Coromandel Peninsula</p>
    <p>Our honey comes to you raw &amp;<br>unpasturized, ensuring it retains<br>all the natural goodness!</p>
    <p>Arohanui<br>Rowan, Noreen &amp; boys</p>
    <p>'Quillbrook' – all thanks to God for his<br>incredible creation!</p>
  </section>

  <address class="contact-details">
    www.quillbrookhoney.co.nz<br>
    27 Tarata Lane<br>
    Whangamata<br>
    New Zealand
  </address>
</main>
</body>
</html>
```